Local Service Business Needing Clear Business Card Design

We are needing a business card design to be made for our power washing company. Business cards will be printed on plastic standard sized cards. We're looking for someone who can make a unique and unforgettable design. Double sided and or single sided concepts would be ideal. Of course keeping in mind we are seeking translucent cards but not married to the idea of having them as the main concern is just to have plastic cards to prevent water damage! :D

More info on our company can be found on brightlakesurfacecare.example

Not looking for a list of our services. Simply applying company info and possibly "Commercial Residential Fleet" on them tastefully and appropriate to design is all thats needed.

Phone number for our company is 877-RNS-CREW or 877-736-2739

Industry/Entity Type

Power Washing

Contact Information for Business Card

Phone, Web URL,

Requirements
Should not have
• Bubbles, water or super distracting graphics. Looking for a simple and clean look. Unfortunately our logo is this way which we may seek to change in the near future.

```html
<!DOCTYPE html>
<html lang="en">
<head>
<meta charset="utf-8">
<title>Bright Lake Surface Care – Business Card</title>
<link rel="stylesheet" href="https://fonts.googleapis.com/css2?family=Alfa+Slab+One&family=Oswald:wght@500&family=Roboto+Condensed:wght@400&display=swap">
<style>
  :root {
    --page-bg: #e9e6e3;
    --card-black: #000000;
    --phone-yellow: #f5e614;
    --url-blue: #19a4ea;
    --text-white: #ffffff;
    --drops-deep: #2c3c73;
    --drops-mid: #3f5592;
    --drops-light: #5a6fa8;
    --wand-yellow: #f2e81c;
    --wand-edge: #3b4a86;
  }
  html, body {
    margin: 0;
    padding: 0;
    width: 1200px;
    height: 900px;
    overflow: hidden;
    background: var(--page-bg);
  }
  .business-card {
    position: absolute;
    left: 100px;
    top: 141px;
    width: 1000px;
    height: 618px;
    background: var(--card-black);
    overflow: hidden;
    box-shadow: 0 10px 30px rgba(0,0,0,0.25);
  }
  .card-art {
    position: absolute;
    inset: 0;
    width: 1000px;
    height: 618px;
  }
  .contact-phone {
    position: absolute;
    left: 56px;
    top: 104px;
    margin: 0;
    font-family: "Alfa Slab One", serif;
    font-size: 50px;
    letter-spacing: 2px;
    color: var(--phone-yellow);
    line-height: 1;
  }
  .contact-url {
    position: absolute;
    left: 56px;
    top: 178px;
    margin: 0;
    font-family: "Roboto Condensed", sans-serif;
    font-size: 31px;
    line-height: 1;
    color: var(--url-blue);
  }
  .contact-url .url-suffix { color: var(--text-white); }
  .service-list {
    position: absolute;
    left: 60px;
    top: 312px;
    margin: 0;
    padding: 0;
    list-style: none;
    font-family: "Oswald", sans-serif;
    font-weight: 500;
    font-size: 52px;
    line-height: 71px;
    color: var(--text-white);
    text-transform: uppercase;
    letter-spacing: -0.5px;
  }
  .brand-name {
    position: absolute;
    left: 520px;
    top: 360px;
    width: 440px;
    margin: 0;
    font-family: "Oswald", sans-serif;
    font-weight: 500;
    font-size: 52px;
    line-height: 1.1;
    color: var(--text-white);
    text-align: center;
    text-transform: uppercase;
  }
</style>
</head>
<body>
  <div class="business-card">
    <svg class="card-art" viewBox="0 0 1000 618" xmlns="http://www.w3.org/2000/svg">
      <defs>
        <radialGradient id="dropsGradient" cx="0.55" cy="0.45" r="0.75">
          <stop offset="0" stop-color="var(--drops-light)"/>
          <stop offset="0.55" stop-color="var(--drops-mid)"/>
          <stop offset="1" stop-color="var(--drops-deep)"/>
        </radialGradient>
      </defs>
      <polygon class="water-drop-field" role="img" aria-label="Photo of water droplets on a blue surface"
               points="634,0 1000,0 1000,618 420,618" fill="url(#dropsGradient)"/>
      <polygon class="pressure-wand" role="img" aria-label="Illustration of a yellow pressure washer wand spraying"
               points="616,0 700,0 640,110 560,300 470,520 455,618 395,618 345,560 420,470 520,280 600,90"
               fill="var(--wand-yellow)" stroke="var(--wand-edge)" stroke-width="3"/>
    </svg>

    <p class="contact-phone">877-736-2739</p>
    <p class="contact-url">brightlakesurfacecare<span class="url-suffix">.example</span></p>

    <ul class="service-list">
      <li>Commercial</li>
      <li>Residential</li>
      <li>Fleet</li>
    </ul>

    <p class="brand-name">Bright Lake<br>Surface Care</p>
  </div>
</body>
</html>
```